magcian / mentalist needs flyer desined to send potentisl clients

I need a design that's contemporary, sharp, fun, and professional that will get the attention of whoever receives the flyer very quickly. This is for a tri-fold flyer design.

I've been performing magic for over 40 years. I've performed close-up,
parlor, and stage shows. I've been an Master of Ceremonies, Key Note
Speaker (using magic during presentations to help build on a point or
topic, while keeping the audience entertained and educated on the topic or
topics the client has asked me to focus). I've worked trade shows and
sales training incorporating magic as well. I did private shows in Las
Vegas and L.A. back in the late 90's as well.

I do have website / wesleytorvandmagic.example for your to check out.

Target Market(s)

The target audience is corporation Event Planners, Marketing and Sales
managers, casino & hotel entertainment directors, as well as private
businesses looking for unique entertainment options.

Industry/Entity Type

Entertainment Industry

Logo Text

Here are a couple of ideas: your mind is my playground, neural entertainer, professor of mysteries, master of your mind

Requirements
Must have
• I like the black and white look (I think it looks nice, but open to other
• ideas and creativity. Being I'm a magician and mentalist, I'd like for
• both venues to be conveyed somehow. My magic is clean and corporate and family friendly.
Nice to have
• I do have website / wesleytorvandmagic.example for your to check out.
• My current business card is attached for review. I'll also attach photos
• I'd like to share, but was unable when I last attempted do sign up. Some
• of the files were too big and I'm not savvy enough to make them smaller,
• but think there might be some potential with a couple.
Should not have
• cartoons or cartoonish graphics. no rabbits, doves, magicians, wands, or top hats.

```html
<!DOCTYPE html>
<html lang="en">
<head>
<meta charset="utf-8">
<title>Wesley Torvand — Tri-fold Brochure</title>
<link href="https://fonts.googleapis.com/css2?family=Jost:ital,wght@0,400;0,500;0,700;0,800;1,400;1,700&display=swap" rel="stylesheet">
<style>
  :root {
    --ink: #050608;
    --paper: #ffffff;
    --stage: #e9e7e3;
    --night: #0b0f1a;
    --haze: #1d2640;
    --glow: #c9d6ff;
    --muted: #d8dbe4;
  }
  * { box-sizing: border-box; margin: 0; padding: 0; }
  html, body { width: 1200px; height: 1200px; overflow: hidden; background: var(--stage); }
  body { font-family: "Jost", sans-serif; color: var(--paper); position: relative; }

  .brochure {
    position: absolute; left: 30px; top: 160px; width: 1140px; height: 880px;
    background: var(--ink);
    box-shadow: 0 10px 30px rgba(0,0,0,.25);
  }
  .panel { position: absolute; top: 0; width: 380px; height: 880px; overflow: hidden; }
  .panel--services { left: 0; }
  .panel--about { left: 380px; border-left: 1px solid #15171c; }
  .panel--cover { left: 760px; border-left: 1px solid #15171c;
    background: radial-gradient(ellipse at 55% 28%, var(--haze) 0%, var(--ink) 60%); }

  .edge { position: absolute; left: 18px; right: 18px; height: 14px; background: var(--paper); }
  .edge--top { top: 10px; }
  .edge--bottom { bottom: 10px; }

  /* Services panel */
  .performance-photo {
    position: absolute; left: 0; top: 24px; width: 380px; height: 300px;
    background: linear-gradient(160deg, #6b4a2c 0%, #3a2616 45%, #0d0a08 100%);
  }
  .headline {
    position: absolute; left: 22px; top: 250px; width: 350px;
    font-weight: 700; font-style: italic; font-size: 22px; line-height: 1.32;
  }
  .headline span { background: var(--ink); padding: 0 6px; }
  .services { position: absolute; left: 22px; top: 420px; width: 336px; }
  .service { margin-bottom: 22px; }
  .service__label {
    display: inline-block; background: var(--paper); color: var(--ink);
    font-weight: 700; font-style: italic; font-size: 14px; padding: 2px 8px; margin-bottom: 6px;
  }
  .service__text { font-style: italic; font-size: 13.5px; line-height: 1.45; color: var(--muted); }

  /* About panel */
  .portrait-frame { position: absolute; left: 60px; top: 100px; width: 260px; height: 260px; }
  .intro {
    position: absolute; left: 40px; top: 420px; width: 300px; text-align: center;
    font-style: italic; font-size: 16px; line-height: 1.5; color: var(--muted);
  }
  .contact { position: absolute; left: 36px; top: 680px; width: 330px; list-style: none; }
  .contact li { display: flex; align-items: center; gap: 10px; font-weight: 500; font-size: 16px; margin-bottom: 10px; }
  .contact svg { width: 18px; height: 18px; flex: none; }

  /* Cover panel */
  .cards-illustration {
    position: absolute; left: 40px; top: 110px; width: 320px; height: 300px; border-radius: 50%;
    background: radial-gradient(ellipse at 50% 50%, rgba(201,214,255,.45) 0%, rgba(60,75,120,.25) 45%, rgba(0,0,0,0) 72%);
  }
  .tagline {
    position: absolute; left: 0; width: 380px; top: 455px; text-align: center;
    font-size: 29px; letter-spacing: 1px; font-weight: 400;
  }
  .tagline-magic {
    position: absolute; left: 0; width: 380px; top: 490px; text-align: center;
    font-size: 92px; font-weight: 800; line-height: 1; letter-spacing: 1px;
    color: var(--paper); text-shadow: 0 0 18px rgba(201,214,255,.35);
  }
  .roles {
    position: absolute; left: 0; width: 380px; top: 690px; text-align: center;
    font-size: 19px; letter-spacing: .5px;
  }

  /* Band crossing the inner and cover panels */
  .band { position: absolute; left: 380px; top: 560px; width: 760px; height: 120px; }
  .band__cta { font-family: "Jost", sans-serif; font-weight: 700; font-style: italic; font-size: 16px; fill: var(--ink); }
  .band__name { font-family: "Jost", sans-serif; font-size: 40px; fill: var(--ink); letter-spacing: 1px; }
</style>
</head>
<body>
  <main class="brochure">
    <section class="panel panel--services">
      <div class="edge edge--top"></div>
      <div class="performance-photo" role="img" aria-label="Photo of Wesley performing with an audience volunteer on stage"></div>
      <h2 class="headline">
        <span>Wesley entertains and presents</span><br>
        <span>key content with magic, humor</span><br>
        <span>and audience participation so</span><br>
        <span>that you learn while you laugh!</span>
      </h2>
      <div class="services">
        <div class="service">
          <div class="service__label">Corporate Magic</div>
          <p class="service__text">Magic at your corporate function adds an element that will distinguish your company from others.</p>
        </div>
        <div class="service">
          <div class="service__label">Healing with Magic</div>
          <p class="service__text">Wesley uses magic to make a difference by helping raise funds and awareness for many different charities.</p>
        </div>
        <div class="service">
          <div class="service__label">Keynote Speaker</div>
          <p class="service__text">Wesley presents key content with magic, humor &amp; audience participation so that you "learn while you laugh"!</p>
        </div>
        <div class="service">
          <div class="service__label">Magic Shows</div>
          <p class="service__text">From close up, parlor, to company picnics to black tie affairs, to private shows or large public venues, Wesley can build a show to fit your needs.</p>
        </div>
      </div>
      <div class="edge edge--bottom"></div>
    </section>

    <section class="panel panel--about">
      <div class="edge edge--top"></div>
      <svg class="portrait-frame" viewBox="0 0 260 260">
        <circle cx="130" cy="130" r="122" fill="none" stroke="#ffffff" stroke-width="14" stroke-dasharray="5 4"/>
        <circle cx="130" cy="130" r="112" fill="#ffffff"/>
        <circle cx="130" cy="130" r="104" fill="#555"/>
      </svg>
      <div role="img" aria-label="Black and white portrait of Wesley performing a trick" style="position:absolute;left:86px;top:126px;width:208px;height:208px;border-radius:50%;background:radial-gradient(circle at 55% 40%,#9a9a9a 0%,#3c3c3c 60%,#111 100%);"></div>
      <p class="intro">I'm a professional entertainer. I've performed all over the country for major corporations which means you're getting tried and true, first-rate entertainment.</p>
      <ul class="contact">
        <li>
          <svg viewBox="0 0 24 24" fill="none" stroke="#fff" stroke-width="2"><path d="M5 3h4l2 5-3 2a12 12 0 0 0 6 6l2-3 5 2v4a2 2 0 0 1-2 2A17 17 0 0 1 3 5a2 2 0 0 1 2-2z"/></svg>
          505-555-0142
        </li>
        <li>
          <svg viewBox="0 0 24 24" fill="none" stroke="#fff" stroke-width="2"><rect x="3" y="5" width="18" height="14"/><path d="M3 5l9 8 9-8"/></svg>
          wesleytorvandmagic@example.com
        </li>
        <li>
          <svg viewBox="0 0 24 24" fill="none" stroke="#fff" stroke-width="2"><circle cx="12" cy="12" r="9"/><path d="M3 12h18M12 3c3 3 3 15 0 18M12 3c-3 3-3 15 0 18"/></svg>
          wesleytorvandmagic.example
        </li>
      </ul>
      <div class="edge edge--bottom"></div>
    </section>

    <section class="panel panel--cover">
      <div class="edge edge--top"></div>
      <div class="cards-illustration" role="img" aria-label="Illustration of a fanned row of playing cards circled by a trail of sparkling stars"></div>
      <p class="tagline">IT'S ALL ABOUT THE</p>
      <h1 class="tagline-magic">MAGIC</h1>
      <p class="roles">MAGICIAN/MENTALIST/ENTERTAINER</p>
      <div class="edge edge--bottom"></div>
    </section>

    <svg class="band" viewBox="0 0 760 120">
      <path d="M0 20 Q190 42 380 48 L760 52 L760 92 L380 88 Q190 82 0 56 Z" fill="#ffffff"/>
      <text class="band__cta" x="22" y="50" transform="rotate(4 190 50)">Contact Wesley today to elevate your event!</text>
      <text class="band__name" x="400" y="84"><tspan font-weight="800">WESLEY</tspan><tspan font-weight="400">TORVAND</tspan></text>
    </svg>
  </main>
</body>
</html>
```